Business card design for a content marketing agency

Need a business card design suitable for a digital marketing agency. Needs to be a bold and creative, high quality design that exudes expertise and professionalism, and instills in prospective new customers a sense of confidence that we are the right company to do business with. Specifications must meet PrintNorvo requirement for extra thick matte stock. Needs to incorporate logo, tagline, name, title, website url, address, city, state, zip code, and mobile number.. I spec'd s single side design but I'm to a double sided design if it's strong and compelling. I like the use of icons associated with contact info, but it's not a requirement. Mostly, the design needs to command attention because it's so good or unusual. I have all kinds of files in large thru small sizes in jpg andpgn. pick from what you need, and let me know if you have questions.

Target Market(s)

CEO, Mktg VP's and small to medium size tech and prof'l service businesses

Industry/Entity Type

Marketing

Contact Information for Business Card

Perry Lindqvist
Chief Executive Officer
418 Wexcombe Lane
Dunmere, MA 01893
perry@quelmarketing.example
www.quelmarketing.example
978-555-2716

Font styles to use
Sans Serif

Colors
0692cd
9bcb3c

Requirements
Must have
• Tagline is "Marketing That Audiences Value".
• Needs to be a bold and creative, high quality design that exudes expertise and professionalism, and instills in prospective new customers a sense of confidence that we are the right company to do business with. Specifications must meet PrintNorvo requirement for extra thick matte stock. Needs to incorporate logo, tagline, name, title, website url, address, city, state, zip code, and mobile number..
Nice to have
• I spec'd s single side design but I'm open to a double sided design if it's strong and compelling. I like the use of icons associated with contact info, but it's not a requirement.
Should not have
• Chose colors that are the same and/or compatible with colors in the logo

```html
<!DOCTYPE html>
<html lang="en">
<head>
<meta charset="utf-8">
<title>Perry Lindqvist – Business Card</title>
<link rel="stylesheet" href="https://fonts.googleapis.com/css2?family=PT+Sans:wght@400;700&display=swap">
<style>
  :root {
    --backdrop: #e9e7e3;
    --card: #ffffff;
    --brand-green: #a6c94a;
    --brand-blue: #0692cd;
    --tagline-blue: #3f9fcf;
    --ink: #111111;
  }
  * { margin: 0; padding: 0; box-sizing: border-box; }
  html, body {
    width: 1200px; height: 895px; overflow: hidden;
    background: var(--backdrop);
    font-family: "PT Sans", sans-serif;
    color: var(--ink);
  }
  .business-card {
    position: absolute; left: 100px; top: 162px;
    width: 1000px; height: 572px;
    background: var(--card);
    box-shadow: 0 10px 30px rgba(0,0,0,0.18);
    overflow: hidden;
  }
  .header-band {
    position: absolute; left: 0; top: 0; width: 100%; height: 200px;
    background: var(--brand-green);
    text-align: center;
  }
  .person-name { position: absolute; left: 0; right: 0; top: 62px; font-size: 44px; font-weight: 400; line-height: 1.1; }
  .person-title { position: absolute; left: 0; right: 0; top: 118px; font-size: 36px; font-weight: 400; line-height: 1.1; }
  .company-name {
    position: absolute; left: 230px; width: 400px; top: 214px;
    display: flex; align-items: center; justify-content: center; gap: 10px;
    font-size: 26px; font-weight: 700; color: var(--brand-blue);
  }
  .company-dot { width: 24px; height: 24px; border-radius: 50%; background: var(--brand-blue); }
  .tagline {
    position: absolute; left: 200px; width: 460px; top: 268px; text-align: center;
    font-size: 29px; color: var(--tagline-blue); white-space: nowrap;
  }
  .icon { position: absolute; }
  .contact { position: absolute; font-size: 21px; line-height: 1.35; white-space: nowrap; }
  .contact-email { right: 40px; top: 280px; text-align: right; }
  .contact-phone { left: 400px; width: 200px; top: 390px; text-align: center; }
  .contact-address { left: 110px; width: 260px; top: 460px; text-align: center; }
</style>
</head>
<body>
  <div class="business-card">
    <div class="header-band">
      <h1 class="person-name">Perry Lindqvist</h1>
      <p class="person-title">Chief Executive Officer</p>
    </div>

    <div class="company-name"><span class="company-dot"></span>Quel Marketing</div>
    <p class="tagline">Marketing That Audiences Value</p>

    <svg class="icon icon-mail" style="left:830px;top:226px" width="46" height="34" viewBox="0 0 46 34" aria-hidden="true">
      <rect x="1.5" y="1.5" width="43" height="31" fill="none" stroke="#111" stroke-width="3"/>
      <rect x="31" y="6" width="9" height="9" fill="#111"/>
      <line x1="7" y1="22" x2="24" y2="22" stroke="#111" stroke-width="2"/>
      <line x1="7" y1="27" x2="20" y2="27" stroke="#111" stroke-width="2"/>
    </svg>
    <p class="contact contact-email">perry@quelmarketing.example<br>www.quelmarketing.example</p>

    <svg class="icon icon-phone" style="left:486px;top:350px" width="28" height="30" viewBox="0 0 24 24" aria-hidden="true">
      <path fill="#111" d="M6.6 10.8a15.1 15.1 0 0 0 6.6 6.6l2.2-2.2c.3-.3.7-.4 1-.2 1.1.4 2.3.6 3.6.6.6 0 1 .4 1 1V20c0 .6-.4 1-1 1A17 17 0 0 1 3 4c0-.6.4-1 1-1h3.5c.6 0 1 .4 1 1 0 1.3.2 2.5.6 3.6.1.3 0 .7-.2 1z"/>
    </svg>
    <p class="contact contact-phone">978-555-2716</p>

    <svg class="icon icon-pin" style="left:224px;top:410px" width="32" height="40" viewBox="0 0 32 40" aria-hidden="true">
      <path fill="#111" d="M16 1C8 1 2 7 2 14.5 2 24 16 39 16 39s14-15 14-24.5C30 7 24 1 16 1z"/>
      <circle cx="16" cy="14.5" r="6" fill="#fff"/>
    </svg>
    <p class="contact contact-address">418 Wexcombe Lane<br>Dunmere, MA 01893</p>
  </div>
</body>
</html>
```